Brevant Business Card

I have a business that is called "Brevant Electrical Products LTD" My company deals with top of the range laptops and mobile phones that are exclusive. I need a business card that will be eye catching but not over complicated.

Target Market(s)

Adults aged 19 to 50
Upper middle class

Industry/Entity Type

Business

Requirements
Must have
• Company name/logo (file attached)
• It must have my contact information which is:

• Name: Dale Marwick

• Position: Managing Director 

• Business Address: 7 Hapton Row, London, W4 9QD

• Contact Number: 02085193604
• Mobile: 07814260537
• Email: info@brevant-goods.co.uk
Nice to have
• Simple and stylish
• Eye catching

```html
<!DOCTYPE html>
<html lang="en">
<head>
<meta charset="utf-8">
<title>Brevant Business Card</title>
<link rel="stylesheet" href="https://fonts.googleapis.com/css2?family=Open+Sans:wght@400;600;700&display=swap">
<style>
  :root {
    --bg: #3b3d40;
    --blue: #1fa9e6;
    --blue-light: #5fc6f2;
    --blue-pale: #9fdcf7;
    --white: #ffffff;
    --paper: #f1f3f5;
    --paper-shade: #d9dde2;
    --ink: #333333;
    --ink-strong: #2a2a2a;
  }
  * { margin: 0; padding: 0; box-sizing: border-box; }
  html, body {
    width: 963px;
    height: 1200px;
    overflow: hidden;
    background: var(--bg);
    font-family: "Open Sans", Arial, sans-serif;
  }
  .canvas {
    position: relative;
    width: 963px;
    height: 1200px;
  }
  .card {
    position: absolute;
    left: 71px;
    width: 820px;
    height: 520px;
    border-radius: 30px;
    overflow: hidden;
    background: var(--paper);
    box-shadow: 0 10px 30px rgba(0,0,0,0.35);
  }
  .card--front { top: 50px; }
  .card--back { top: 630px; }
  .card__art {
    position: absolute;
    inset: 0;
    width: 100%;
    height: 100%;
  }
  .brand-name {
    position: absolute;
    color: var(--white);
    font-weight: 400;
    letter-spacing: 0.04em;
    text-transform: uppercase;
    line-height: 1;
    white-space: nowrap;
  }
  .card--front .brand-name { left: 62px; top: 58px; font-size: 62px; }
  .card--back .brand-name { right: 70px; top: 150px; font-size: 96px; }

  .person {
    position: absolute;
    left: 70px;
    top: 245px;
    color: var(--ink);
    white-space: nowrap;
  }
  .person__name { font-size: 25px; font-weight: 700; color: var(--ink-strong); }
  .person__role { font-size: 23px; font-weight: 400; margin-top: 2px; }

  .contact-list {
    position: absolute;
    left: 82px;
    top: 338px;
    list-style: none;
    font-size: 21px;
    color: var(--ink);
    line-height: 1.35;
  }
  .contact-list__item { white-space: nowrap; }
  .contact-list__label { display: inline-block; width: 44px; }

  .company {
    position: absolute;
    left: 448px;
    top: 215px;
    color: var(--blue);
    font-weight: 700;
    font-size: 23px;
    line-height: 1.2;
    white-space: nowrap;
  }
  .address {
    position: absolute;
    left: 458px;
    top: 295px;
    font-size: 21px;
    color: var(--ink);
    line-height: 1.4;
    font-style: normal;
    white-space: nowrap;
  }
  .website {
    position: absolute;
    left: 80px;
    bottom: 48px;
    color: var(--blue);
    font-weight: 700;
    font-size: 32px;
    letter-spacing: 0.02em;
    white-space: nowrap;
  }
</style>
</head>
<body>
<main class="canvas">

  <section class="card card--front" aria-label="Business card front">
    <svg class="card__art" viewBox="0 0 820 520" preserveAspectRatio="none" aria-hidden="true">
      <defs>
        <linearGradient id="frontPaper" x1="0" y1="0" x2="0" y2="1">
          <stop offset="0" stop-color="#ffffff"/>
          <stop offset="1" stop-color="#dde1e6"/>
        </linearGradient>
        <linearGradient id="frontBlue" x1="0" y1="0" x2="1" y2="1">
          <stop offset="0" stop-color="#1fa9e6"/>
          <stop offset="1" stop-color="#2bb3ec"/>
        </linearGradient>
      </defs>
      <rect width="820" height="520" fill="url(#frontPaper)"/>
      <path d="M0,0 H820 V95 C690,75 560,180 400,188 C250,195 110,180 0,200 Z" fill="url(#frontBlue)"/>
      <path d="M0,0 H820 V45 C700,30 560,115 390,125 C240,134 120,105 0,125 Z" fill="#5fc6f2" opacity="0.35"/>
      <path d="M0,200 C110,180 250,195 400,188 C560,180 690,75 820,95 V110 C690,92 560,196 400,204 C250,211 110,198 0,215 Z" fill="#ffffff" opacity="0.75"/>
    </svg>

    <div class="brand-name">Brevant</div>

    <div class="person">
      <div class="person__name">Dale Marwick</div>
      <div class="person__role">Managing Director</div>
    </div>

    <ul class="contact-list">
      <li class="contact-list__item"><span class="contact-list__label">T |</span>02085193604</li>
      <li class="contact-list__item"><span class="contact-list__label">M |</span>07814260537</li>
      <li class="contact-list__item"><span class="contact-list__label">E |</span>info@brevant-goods.co.uk</li>
    </ul>

    <div class="company">BREVANT<br>Electrical Products Ltd.</div>
    <address class="address">7 Hapton Row,<br>London,<br>W4 9QD</address>
  </section>

  <section class="card card--back" aria-label="Business card back">
    <svg class="card__art" viewBox="0 0 820 520" preserveAspectRatio="none" aria-hidden="true">
      <defs>
        <linearGradient id="backBlue" x1="0" y1="0" x2="1" y2="1">
          <stop offset="0" stop-color="#1ba6e4"/>
          <stop offset="1" stop-color="#30b6ee"/>
        </linearGradient>
        <linearGradient id="backPaper" x1="0" y1="0" x2="0" y2="1">
          <stop offset="0" stop-color="#ffffff"/>
          <stop offset="1" stop-color="#d9dde2"/>
        </linearGradient>
      </defs>
      <rect width="820" height="520" fill="url(#backBlue)"/>
      <path d="M0,0 H820 V90 C660,40 520,150 330,110 C200,84 100,40 0,70 Z" fill="#5fc6f2" opacity="0.3"/>
      <path d="M0,230 C120,180 260,210 380,260 C500,305 640,300 820,250 V300 C650,340 500,340 380,300 C250,255 120,230 0,270 Z" fill="#9fdcf7" opacity="0.3"/>
      <path d="M0,440 C140,380 300,340 480,340 C620,340 720,330 820,300 V520 H0 Z" fill="url(#backPaper)"/>
      <path d="M0,440 C140,380 300,340 480,340 C620,340 720,330 820,300 V320 C720,350 620,362 480,362 C320,364 160,400 0,460 Z" fill="#ffffff" opacity="0.6"/>
    </svg>

    <div class="brand-name">Brevant</div>
    <div class="website">www.brevant-goods.co.uk</div>
  </section>

</main>
</body>
</html>
```